Lumenhart Media-Works Stationary
Stationary for high tech media company
Project: Lumenhart Media-Works Stationary
Creative Brief
Professional
Rolf Kestermann, M.Ed.
48260 Marlowe Livonia, Michigan 48397
rk@lumenhartmw.com
www.lumenhartmw.com
You could add on the the card and/or stationary in a small font the following description: Full Service Legal Video - Certified Court Reporters - Forensic Animation - Attorney Website Development - Litigation Graphics
Concepts
BUSINESS CARD, LETTERHEAD ENVELOPES FOR VIDEO PRODUCTION COMPANY
q7fernbridge q7fernbridge
it does need to be a one sided business card because it will have a peel off back. so the description does need to fit on one side with the rest of the info
I would like to have on the business cards and stationary the following description in a small front: Full Services Legal Video - Certified Court Reporters - Forensic Animation - Attorney Website Development - Litigation Graphics. I would will like to set the full stations set, not just the business card

```html
<!DOCTYPE html>
<html lang="en">
<head>
<meta charset="utf-8">
<title>Lumenhart Media-Works Business Card</title>
<link href="https://fonts.googleapis.com/css2?family=Montserrat:wght@400;500;700&display=swap" rel="stylesheet">
<style>
  :root {
    --page-bg: #e9e9ec;
    --card-face: #f6f7f9;
    --brand-blue: #24389a;
    --brand-blue-deep: #17246f;
    --brand-gold: #f2b41c;
    --brand-gold-light: #ffd85a;
    --logo-ink: #1f2c7c;
    --tagline-ink: #6b7080;
    --panel-text: #ffffff;
    --panel-text-soft: #dfe4ff;
  }
  * { margin: 0; padding: 0; box-sizing: border-box; }
  html, body {
    width: 1200px; height: 768px; overflow: hidden;
    background: var(--page-bg);
    font-family: "Montserrat", Arial, sans-serif;
  }
  .business-card {
    position: absolute; left: 150px; top: 124px;
    width: 900px; height: 520px;
    background: var(--card-face);
    border-radius: 6px;
    box-shadow: 0 10px 30px rgba(20, 30, 70, 0.18);
    overflow: hidden;
  }
  .card-shapes { position: absolute; inset: 0; }
  .brand-lockup {
    position: absolute; left: 40px; top: 206px;
  }
  .brand-name {
    display: flex; align-items: center; gap: 14px;
    font-size: 66px; font-weight: 700; color: var(--logo-ink);
    letter-spacing: -1px; line-height: 1;
  }
  .brand-dot {
    width: 22px; height: 22px; border-radius: 50%;
    background: var(--brand-gold); flex: none;
  }
  .brand-tagline {
    margin-top: 10px; margin-left: 36px;
    font-size: 13px; font-weight: 500; letter-spacing: 2.6px;
    color: var(--tagline-ink); white-space: nowrap;
  }
  .contact-panel {
    position: absolute; left: 580px; top: 0; width: 300px; height: 100%;
    color: var(--panel-text);
  }
  .person-name { position: absolute; top: 86px; font-size: 25px; font-weight: 500; white-space: nowrap; }
  .person-role { position: absolute; top: 122px; font-size: 18px; color: var(--panel-text-soft); }
  .office-address {
    position: absolute; top: 196px; font-size: 16px; line-height: 1.55;
    color: var(--panel-text-soft); white-space: nowrap;
  }
  .contact-list {
    position: absolute; top: 296px; list-style: none;
    font-size: 14.5px; color: var(--panel-text-soft);
  }
  .contact-list li {
    display: flex; align-items: center; gap: 12px; height: 28px; white-space: nowrap;
  }
  .contact-icon { width: 14px; height: 14px; fill: var(--panel-text); flex: none; }
  .contact-icon.outline { fill: none; stroke: var(--panel-text); stroke-width: 1.6; }
</style>
</head>
<body>
  <div class="business-card">
    <svg class="card-shapes" width="900" height="520" viewBox="0 0 900 520">
      <defs>
        <linearGradient id="panelBlue" x1="0" y1="0" x2="1" y2="1">
          <stop offset="0" stop-color="#24389a"/>
          <stop offset="1" stop-color="#17246f"/>
        </linearGradient>
        <linearGradient id="goldArc" x1="0" y1="0" x2="0" y2="1">
          <stop offset="0" stop-color="#ffd85a"/>
          <stop offset="1" stop-color="#f2b41c"/>
        </linearGradient>
      </defs>
      <path d="M455 0 Q548 250 470 520 L498 520 Q570 250 482 0 Z" fill="url(#goldArc)"/>
      <path d="M478 0 Q566 250 494 520 L900 520 L900 0 Z" fill="url(#panelBlue)"/>
    </svg>

    <div class="brand-lockup">
      <div class="brand-name"><span class="brand-dot"></span>Lumenhart</div>
      <div class="brand-tagline">Media-Works Communications</div>
    </div>

    <div class="contact-panel">
      <div class="person-name">Rolf Kestermann</div>
      <div class="person-role">consultant</div>
      <div class="office-address">48260 Marlowe<br>Livonia, MI 48397</div>
      <ul class="contact-list">
        <li><svg class="contact-icon" viewBox="0 0 16 16"><path d="M4 1h3l1 4-2 1.5a9 9 0 0 0 3.5 3.5L11 8l4 1v3c0 1.1-.9 2-2 2A12 12 0 0 1 2 3c0-1.1.9-2 2-2z"/></svg>012 555 0148</li>
        <li><svg class="contact-icon" viewBox="0 0 16 16"><rect x="4" y="1" width="8" height="14" rx="1.5"/></svg>012 555 0149</li>
        <li><svg class="contact-icon" viewBox="0 0 16 16"><path d="M4 1h8v4H4zM1 6h14v6h-3v3H4v-3H1z"/></svg>012 555 0150</li>
        <li><svg class="contact-icon outline" viewBox="0 0 16 16"><path d="M1.5 3.5h13v9h-13zM1.5 3.5l6.5 5 6.5-5"/></svg>rk@lumenhartmw.com</li>
        <li><svg class="contact-icon outline" viewBox="0 0 16 16"><circle cx="8" cy="8" r="6.5"/><path d="M1.5 8h13M8 1.5c-2.5 3-2.5 10 0 13M8 1.5c2.5 3 2.5 10 0 13"/></svg>www.lumenhartmw.com</li>
      </ul>
    </div>
  </div>
</body>
</html>
```